I need creative and unique business card design using my company logo. Ok to change logo color. We are a small brokerage doing both Real Estate and Mortgage services. Need to have the follow on business card;
1. agent name - Nora Velden - Realtor
2. cell - 949-555-0182
3. license number - DRE 07164392
4. business name - Bright Keys & Lending, Inc
5. business office - 626-555-0147
6. business address - 214 W. Marlowe Ave #308, Linden Vale CA 91840
7. business logo - attached (ok to use different color on logo)

```html
<!DOCTYPE html>
<html lang="en">
<head>
<meta charset="utf-8">
<title>Nora Velden – Business Card</title>
<link href="https://fonts.googleapis.com/css2?family=Arimo:wght@400;700&display=swap" rel="stylesheet">
<style>
  :root {
    --backdrop: #1c1c1c;
    --card-white: #ffffff;
    --brand-navy: #2455a4;
    --brand-sky: #3d93d3;
    --text-grey: #6e6e6e;
    --rule-grey: #8a8a8a;
    --back-blue: #2c65b0;
    --back-white: #ffffff;
  }
  * { margin: 0; padding: 0; box-sizing: border-box; }
  html, body {
    width: 1200px; height: 1059px; overflow: hidden;
    background: var(--backdrop);
    font-family: "Arimo", Arial, sans-serif;
  }
  .canvas { position: relative; width: 1200px; height: 1059px; }

  .card {
    position: absolute;
    box-shadow: 0 10px 30px rgba(0,0,0,.55);
  }
  .card-front {
    left: 258px; top: 89px; width: 689px; height: 394px;
    background: var(--card-white);
  }
  .card-back {
    left: 252px; top: 541px; width: 701px; height: 400px;
    background: var(--back-blue);
  }

  /* Front: identity block */
  .identity {
    position: absolute; right: 361px; top: 160px;
    text-align: right; line-height: 1.1;
  }
  .agent-name { font-size: 24px; font-weight: 700; letter-spacing: .2px; }
  .agent-name .first { color: var(--brand-navy); }
  .agent-name .last { color: var(--brand-sky); }
  .agent-role { font-size: 18px; color: var(--text-grey); margin-top: 2px; }
  .agent-license { font-size: 18px; color: var(--text-grey); margin-top: 3px; }
  .agent-license .label { color: var(--brand-sky); }

  .divider {
    position: absolute; left: 344px; top: 150px;
    width: 1.5px; height: 94px; background: var(--rule-grey);
  }

  .contact {
    position: absolute; left: 362px; top: 140px;
    font-size: 18.5px; color: var(--text-grey); line-height: 28px;
    list-style: none;
  }
  .contact li { display: flex; align-items: center; white-space: nowrap; }
  .contact .icon { width: 16px; height: 16px; margin-right: 8px; flex: none; }
  .contact .address { display: block; }

  /* Back */
  .back-pattern {
    position: absolute; inset: 0;
    background: linear-gradient(180deg, #2d67b3, #2a61aa);
  }
  .brand {
    position: absolute; left: 0; right: 0; top: 86px;
    text-align: center; color: var(--back-white);
  }
  .brand-square {
    display: block; width: 63px; height: 63px; margin: 0 auto 30px;
    background: var(--back-white);
  }
  .brand-name { font-size: 28px; font-weight: 700; letter-spacing: 8px; line-height: 1; padding-left: 8px; }
  .brand-sub { font-size: 13px; font-weight: 700; letter-spacing: 4.2px; margin-top: 8px; padding-left: 4px; }
</style>
</head>
<body>
<main class="canvas">
  <section class="card card-front" aria-label="Card front">
    <div class="identity">
      <p class="agent-name"><span class="first">NORA</span> <span class="last">VELDEN</span></p>
      <p class="agent-role">Realtor</p>
      <p class="agent-license"><span class="label">Lic No:</span> DRE 07164392</p>
    </div>
    <div class="divider"></div>
    <ul class="contact">
      <li>
        <svg class="icon" viewBox="0 0 16 16" aria-hidden="true">
          <path d="M4 2 L6.3 5 L5 6.6 C5.8 8.4 7.3 10 9.2 11 L10.8 9.6 L14 11.9 L12.5 14.2 C7.2 13.6 2.5 8.8 2 3.5 Z" fill="none" stroke="var(--brand-navy)" stroke-width="1.5" stroke-linejoin="round"/>
          <path d="M9 2.5 A4.5 4.5 0 0 1 13.5 7 M9 5 A2 2 0 0 1 11 7" fill="none" stroke="var(--brand-sky)" stroke-width="1.3"/>
        </svg>
        949-555-0182
      </li>
      <li>
        <svg class="icon" viewBox="0 0 16 16" aria-hidden="true">
          <rect x="1.5" y="3.5" width="13" height="9.5" rx="1.5" fill="none" stroke="var(--brand-navy)" stroke-width="1.5"/>
          <path d="M2 4.5 L8 9 L14 4.5" fill="none" stroke="var(--brand-sky)" stroke-width="1.4"/>
        </svg>
        626-555-0147
      </li>
      <li class="address">214 W. Marlowe Ave</li>
      <li class="address">#308, Linden Vale CA 91840</li>
    </ul>
  </section>

  <section class="card card-back" aria-label="Card back">
    <div class="back-pattern" role="img" aria-label="Faint embossed repeating brand pattern on blue"></div>
    <div class="brand">
      <span class="brand-square" aria-hidden="true"></span>
      <p class="brand-name">BRIGHT KEYS</p>
      <p class="brand-sub">&amp; LENDING, INC</p>
    </div>
  </section>
</main>
</body>
</html>
```